Business Card Design for BrightlaneReach.com

--I need a business card design for my company BrightlaneReach.com

I have attached my logo...I want the brightlane reach logo on the front of the business card, and then I want The Brightlane Chief on the back of it with my information.

I would like to see a light colored background as well as a dark colored background

FRONT:
BRIGHTLANE REACH LOGO
247 E. Pelham Row
5th Floor
San Diego CA 92384
www.BrightlaneReach.com

Advanced Website & App Development
Websites, Apps, Online Voucher Systems

Leading Edge Marketing Services
SMS, VB, SMM, SEM,

BACK:
BRIGHTLANE CHIEF LOGO
Dorian Welker
The Brightlane Chief
Call Or Text: 555-204-3378
Dorian@BrightlaneChief.com
www.BrightlaneChief.com

Target Market(s)

small business owners

Industry/Entity Type

Business Consultant

Contact Information for Business Card

FRONT:
BRIGHTLANE REACH LOGO
247 E. Pelham Row
5th Floor
San Diego CA 92384
www.BrightlaneReach.com

SMS, VB, SMM, SEM,

BACK:
BRIGHTLANE CHIEF LOGO
Dorian Welker
The Brightlane Chief
Dorian@BrightlaneChief.com
www.BrightlaneChief.com

Requirements
Must have
• add this quote on it somewhere, anywhere,preferrably on back
• "The Fastest Way To Success Is To Take Action”
• — Dorian Welker, Brightlane Chief
Nice to have
• open
Should not have
• red

```html
<!DOCTYPE html>
<html lang="en">
<head>
<meta charset="utf-8">
<title>Brightlane Reach – Business Cards</title>
<link rel="stylesheet" href="https://fonts.googleapis.com/css2?family=Arimo:wght@400;700&display=swap">
<style>
  :root {
    --backdrop: #2c2c2e;
    --card: #ffffff;
    --brand-blue: #0f76b4;
    --swoosh-grey: #6d6e71;
    --text-grey: #58595b;
    --rule-grey: #8a8b8e;
  }
  * { box-sizing: border-box; margin: 0; padding: 0; }
  html, body {
    width: 1200px; height: 1189px; overflow: hidden;
    background: var(--backdrop);
    font-family: "Arimo", Arial, sans-serif;
  }
  .card {
    position: absolute; left: 160px;
    width: 880px; height: 503px;
    background: var(--card);
    border-radius: 26px;
    overflow: hidden;
    box-shadow: 0 14px 30px rgba(0,0,0,.45);
  }
  .card--chief { top: 60px; }
  .card--reach { top: 626px; }
  .swoosh { position: absolute; inset: 0; width: 100%; height: 100%; }
  .swoosh__band { fill: var(--brand-blue); }
  .swoosh__accent { fill: none; stroke: var(--swoosh-grey); stroke-width: 7; }

  .brand-name {
    position: absolute;
    color: var(--brand-blue);
    font-weight: 400;
    letter-spacing: 2px;
    white-space: nowrap;
    line-height: 1;
  }
  .rule { position: absolute; height: 1px; background: var(--rule-grey); }

  /* Chief card */
  .card--chief .brand-name { left: 80px; top: 62px; font-size: 56px; }
  .contact { position: absolute; left: 140px; top: 160px; width: 500px; text-align: center; }
  .contact__name { color: var(--brand-blue); font-weight: 700; font-size: 28px; line-height: 32px; letter-spacing: .5px; }
  .contact__title { color: var(--text-grey); font-size: 17px; line-height: 20px; margin-top: 2px; }
  .contact__lines { color: var(--text-grey); font-size: 18px; line-height: 24px; margin-top: 20px; }
  .contact__web { color: var(--text-grey); font-size: 18px; line-height: 24px; margin-top: 20px; }
  .accent { color: var(--brand-blue); }

  /* Reach card */
  .card--reach .brand-name { left: 0; width: 800px; text-align: center; top: 56px; font-size: 54px; }
  .services { position: absolute; left: 0; width: 800px; top: 150px; text-align: center; color: var(--text-grey); font-size: 18px; line-height: 23px; }
  .services__highlight { color: var(--brand-blue); font-weight: 700; font-size: 20px; line-height: 25px; margin-top: 2px; }
  .address { position: absolute; left: 0; width: 800px; top: 274px; text-align: center; color: var(--text-grey); font-size: 20px; line-height: 26px; }
</style>
</head>
<body>

<section class="card card--chief" aria-label="Back of card">
  <svg class="swoosh" viewBox="0 0 880 503" preserveAspectRatio="none" aria-hidden="true">
    <path class="swoosh__band" d="M0,430 C500,430 780,360 880,180 L880,503 L0,503 Z"/>
    <path class="swoosh__accent" d="M0,416 C500,416 770,346 866,164"/>
  </svg>
  <div class="brand-name">BRIGHTLANE CHIEF</div>
  <div class="rule" style="left:130px; top:146px; width:520px;"></div>
  <div class="contact">
    <div class="contact__name">DORIAN WELKER</div>
    <div class="contact__title">The Brightlane Chief</div>
    <div class="contact__lines">
      <div>Call Or Text: 555-204-3378</div>
      <div>Dorian@BrightlaneChief.com</div>
    </div>
    <div class="contact__web">www.<span class="accent">BrightlaneChief</span>.com</div>
  </div>
  <div class="rule" style="left:130px; top:291px; width:520px;"></div>
</section>

<section class="card card--reach" aria-label="Front of card">
  <svg class="swoosh" viewBox="0 0 880 503" preserveAspectRatio="none" aria-hidden="true">
    <path class="swoosh__band" d="M0,430 C500,430 780,360 880,180 L880,503 L0,503 Z"/>
    <path class="swoosh__accent" d="M0,416 C500,416 770,346 866,164"/>
  </svg>
  <div class="brand-name">BRIGHTLANE REACH</div>
  <div class="rule" style="left:130px; top:132px; width:540px;"></div>
  <div class="services">
    <div>Advanced Website &amp; App Development</div>
    <div>Websites, Apps, Online Voucher Systems</div>
    <div class="services__highlight">Leading Edge Marketing Services</div>
    <div>SMS&nbsp; | &nbsp;VB&nbsp; | &nbsp;SMM&nbsp; | &nbsp;SEM</div>
  </div>
  <div class="rule" style="left:130px; top:263px; width:540px;"></div>
  <div class="address">
    <div>247 E. Pelham Row, 5th Floor, San Diego CA 92384</div>
    <div>www.<span class="accent">BrightlaneReach</span>.com</div>
  </div>
</section>

</body>
</html>
```